Formation, reconversion, une autre version de vous - Accompagner vos transformations

Je suis formatrice pour adultes, responsable pédagogique et conseillère en insertion professionnelle.
Ma mission est d'accompagner l'employabilité de différents publics, soit par la formation, soit en concevant des projets d'insertion professionnelle et pédagogiques.

L'idée est de présenter 1 - mon offre, qui répond à 2 - un besoin, 3 - pour divers publics, 4 - en me basant sur ma propre
J'ai fait une power point que je joins pour que vous ayez le contenu initial. Attention : le design ne me convient pas, trop chargé.
J'ai besoin d'un design de power point :
- en noir et blanc avec des touches de vert (pour reprendre le code couleur de mon logo). Seules les photos seront en couleurs
- Sobre mais percutant
- Je préfère les formes carrées et rectangulaires aux formes rondes
- police de caractère : Trebuchet MS
- incluant le logo en pied de page sur chaque slide
- incluant un QR code (joint) modifiable
- incluant des photos de personnes africaines et européennes contextualisées en environnement professionnel ou de formation ; souriant

Target Market(s)

Je propose mes services à : - des organismes de formation ( ex: centres de formation publics et privés, associations, ) - des entreprises qui souhaitent être accompagnées pour la transition professionnelle de leurs salariés dans le cadre d'une conduite du changement - des TPME (créateurs d'entreprises en croissance) car lorsqu'un créateur d'entreprise atteint une certaine croissance, il a besoin de recruter et d'être accompagné pour cela. J'ai prospecté des clients récemment et dois leur envoyer une plaquette de mon offre de services rapidement.

Font styles to use
Script
Other font styles liked:
• TRebuchet MS

Colors

Designer to choose only greyscale colors for use in the design.

Requirements
Must have
• Des photos de personnes africaines et européennes souriantes, épanouies en couleurs (seules touches de couleur de la ppoint).
Should not have
• Formes rondes

```html
<!DOCTYPE html>
<html lang="fr">
<head>
<meta charset="utf-8">
<title>NOVA – Formation | Reconversion</title>
<link href="https://fonts.googleapis.com/css2?family=Kaushan+Script&family=PT+Sans:wght@400;700&display=swap" rel="stylesheet">
<style>
:root{
  --green-dark:#0f4d1c;
  --green:#1f7a2c;
  --green-bright:#35b145;
  --ink:#111;
  --paper:#fff;
  --teal:#3cbcb0;
  --blue:#1d63c6;
  --red:#e8334a;
  --purple:#4a2a8a;
  --lime:#8bc34a;
}
*{box-sizing:border-box;margin:0;padding:0}
html,body{width:1200px;height:1200px;overflow:hidden;background:var(--paper)}
body{position:relative;font-family:"PT Sans",sans-serif;color:var(--ink)}
.slide{position:absolute;width:259px;height:146px;background:var(--paper);overflow:hidden;box-shadow:0 1px 4px rgba(0,0,0,.25)}
.c1{left:137px}.c2{left:470px}.c3{left:804px}
.r1{top:44px}.r2{top:206px}.r3{top:366px}.r4{top:527px}.r5{top:688px}.r6{top:849px}.r7{top:1010px}
.photo{position:absolute}
.title{position:absolute;font-family:"Kaushan Script",cursive;color:var(--green-dark);font-size:11px;white-space:nowrap}
.center{left:0;right:0;text-align:center}
.txt{position:absolute;font-size:3.6px;line-height:1.3;color:#222}
.foot-logo{position:absolute;left:10px;bottom:4px;font-weight:700;font-size:6px;letter-spacing:.5px;display:flex;align-items:center;gap:1.5px}
.foot-logo i{display:block;width:3px;height:3px;background:var(--green)}
.foot-url{position:absolute;right:14px;bottom:4px;font-size:2.6px;color:#999}
.logo{position:absolute;font-weight:700;letter-spacing:2px;display:flex;align-items:center;gap:3px;line-height:1}
.logo i{display:block;background:var(--green)}
.tagline{position:absolute;font-weight:700;font-size:4.6px;letter-spacing:.6px;line-height:1.25}
.vname{position:absolute;font-size:3.2px;font-weight:700;transform:rotate(-90deg);transform-origin:left top;white-space:nowrap;letter-spacing:.3px}
.ico{position:absolute;width:14px;height:14px;display:flex;align-items:center;justify-content:center}
.ico b{display:block;width:7px;height:5px;border:1px solid #fff}
.bullet{position:absolute;font-size:3.8px;line-height:1.3;color:#222;padding-left:8px}
.bullet:before{content:"";position:absolute;left:0;top:1px;width:3.5px;height:3.5px;background:var(--green-dark)}
.cat-head{position:absolute;font-size:3.6px;font-weight:700}
.cat-list{position:absolute;font-size:2.8px;line-height:1.4;color:#444}
.cat-bar{position:absolute;width:100px;height:11px;color:#fff;font-size:3.6px;display:flex;align-items:center;padding-left:20px}
.band{position:absolute;left:0;right:0;background:var(--green-dark);color:#fff;display:flex;align-items:center;justify-content:space-around;font-size:3.4px}
.band span,.contact-col span{display:flex;align-items:center;gap:2px}
.band span i,.contact-col span i{display:block;width:5px;height:5px;background:#fff}
.client{position:absolute;font-size:7px;font-weight:700;color:#555;display:flex;align-items:center;gap:3px;white-space:nowrap}
.client i{display:block;width:7px;height:7px;background:#999}
.milestone{position:absolute;width:50px}
.milestone .yr{font-size:3px;margin-bottom:1px}
.milestone .hd{color:#fff;font-size:2.4px;padding:1px;line-height:1.25}
.milestone .bd{font-size:2.4px;padding:1px;line-height:1.25;background:#fff}
.hex{position:absolute;width:42px;height:36px;clip-path:polygon(25% 0,75% 0,100% 50%,75% 100%,25% 100%,0 50%)}
.hex-in{position:absolute;width:38px;height:32px;clip-path:polygon(25% 0,75% 0,100% 50%,75% 100%,25% 100%,0 50%);background:#fff;display:flex;align-items:center;justify-content:center;font-size:3.4px;text-align:center;padding:0 5px;line-height:1.2}
</style>
</head>
<body>

<!-- Row 1 -->
<section class="slide c1 r1">
  <div class="photo" style="inset:0;background:linear-gradient(110deg,#1f5e2a 0%,#4d7d55 30%,#b9c2ba 65%,#e3e5e3 100%)" role="img" aria-label="Couloir d'architecture moderne baigné de lumière, teinté de vert"></div>
  <div class="vname" style="left:30px;top:98px">MAËLLE DORÉ</div>
  <div class="logo" style="left:38px;top:45px;font-size:30px">NOVA<i style="width:8px;height:8px"></i></div>
  <div style="position:absolute;left:146px;top:46px;font-size:7.2px;line-height:1.25;color:#1b1b1b">“L'ARCHITECTE DE<br>VOS PROJETS<br>PROFESSIONNELS”</div>
  <div class="tagline" style="left:38px;top:90px">FORMATION | RECONVERSION<br>UNE AUTRE VERSION DE VOUS</div>
  <div class="foot-url" style="right:70px;color:#333">www.novaformation.fr/maelle-dore</div>
</section>

<section class="slide c2 r1">
  <div class="photo" style="left:110px;top:0;right:0;bottom:0;background:linear-gradient(90deg,#e9ebe9,#a9b1aa 60%,#6f7a70)" role="img" aria-label="Tour de bureaux aux courbes blanches vue en contre-plongée"></div>
  <div class="photo" style="inset:0;background:linear-gradient(115deg,#1e6a2a 0%,rgba(30,106,42,0) 35%)"></div>
  <div class="vname" style="left:20px;top:96px">MAËLLE DORÉ</div>
  <div class="logo" style="left:30px;top:38px;font-size:28px">NOVA<i style="width:8px;height:8px"></i></div>
  <div class="tagline" style="left:30px;top:82px">FORMATION | RECONVERSION<br>UNE AUTRE VERSION DE VOUS</div>
  <div style="position:absolute;left:26px;top:102px;font-size:6.6px;line-height:1.25;text-align:center;width:110px">“L'ARCHITECTE DE VOS<br>PROJETS PROFESSIONNELS”</div>
  <div class="foot-url" style="right:70px;color:#333">www.novaformation.fr/maelle-dore</div>
</section>

<section class="slide c3 r1">
  <div class="photo" style="left:126px;top:0;right:0;bottom:0;background:linear-gradient(135deg,#1f6d2b,#5f8f63 50%,#a7b9a8)" role="img" aria-label="Équipe souriante réunie, mains levées en signe de réussite"></div>
  <div class="title" style="left:12px;top:35px;font-size:10px;line-height:1.3">A PROPOS<br>Réinventons-Vous!</div>
  <div class="txt" style="left:12px;top:68px;width:108px;font-style:italic;font-size:3.5px">« La formation est, selon nous, un outil stratégique au service du développement d'organisations performantes. C'est aussi le moyen le plus adéquat, pour les entreprises, de se réinventer et donc de s'adapter à un monde en constante mutation professionnelle. Former, transformer, performer. Voilà nos maîtres mots. »</div>
  <div class="foot-logo">NOVA<i></i></div>
</section>

<!-- Row 2 -->
<section class="slide c1 r2">
  <div class="title center" style="top:8px;font-size:10px">Ton histoire fait ta force »</div>
  <div class="txt" style="left:30px;right:30px;top:23px;text-align:center">Mon parcours est centré sur l'humain, la co-construction par la communication, la transmission, le métissage culturel et la performance des organisations</div>
  <div class="photo" style="left:28px;top:34px;width:204px;height:100px;background:linear-gradient(120deg,#eef0ee,#e1e5e1 50%,#eef0ee)" role="img" aria-label="Frise illustrée du parcours professionnel de 2000 à aujourd'hui"></div>
  <div class="milestone" style="left:32px;top:36px">
    <div class="yr" style="color:var(--purple)">2000-2008</div>
    <div class="hd" style="background:var(--purple)">Gestionnaire de projets de développement</div>
    <div class="bd" style="border:.5px solid var(--purple)">Je développe une capacité de travail en mode projet</div>
  </div>
  <div class="milestone" style="left:178px;top:36px">
    <div class="yr" style="color:var(--blue)">2008-2017</div>
    <div class="hd" style="background:var(--blue)">Gestionnaire d'une fondation d'entreprise</div>
    <div class="bd" style="border:.5px solid var(--blue)">Je décrypte les enjeux des organisations</div>
  </div>
  <div class="milestone" style="left:44px;top:82px">
    <div class="yr" style="color:var(--green)">Depuis 2017</div>
    <div class="hd" style="background:var(--green)">Formatrice consultante en communication</div>
    <div class="bd" style="border:.5px solid var(--green)">Je renforce mon sens de l'écoute</div>
  </div>
  <div class="milestone" style="left:172px;top:82px;width:58px">
    <div class="yr" style="color:var(--red)">Depuis 2020</div>
    <div class="hd" style="background:var(--red)">Conseillère en insertion, responsable pédagogique</div>
    <div class="bd" style="border:.5px solid var(--red)">Empathie, écoute, patience, adaptation</div>
  </div>
  <div class="foot-logo">NOVA<i></i></div>
  <div class="foot-url">www.novaformation.fr/maelle-dore</div>
</section>

<section class="slide c2 r2">
  <div class="photo" style="left:0;top:0;width:65px;bottom:0;background:linear-gradient(160deg,#2e5560,#7e97a0 55%,#37424a)" role="img" aria-label="Main pointant l'écran d'un ordinateur portable"></div>
  <div class="title" style="left:76px;top:18px;font-size:10px">Notre offre de services...Aujourd'hui</div>
  <div class="ico" style="left:86px;top:54px;background:var(--green-dark)"><b></b></div>
  <div class="txt" style="left:110px;top:55px;width:135px">Faire de la <b>formation par l'innovation</b> un tremplin pour la montée en compétences managériales et comportementales des salariés en devenir et actuels, au profit des entreprises.</div>
  <div class="ico" style="left:86px;top:79px;background:var(--green)"><b></b></div>
  <div class="txt" style="left:110px;top:80px;width:135px"><b>Développer ou renforcer</b> la confiance et les compétences des publics éloignés de l'emploi qui se destinent à des métiers de l'accompagnement.</div>
  <div class="ico" style="left:86px;top:104px;background:var(--green-bright)"><b></b></div>
  <div class="txt" style="left:110px;top:105px;width:135px"><b>Concevoir</b> des projets d'ingénierie pédagogique et d'insertion professionnelle adaptés à un monde du travail et à un marché de l'emploi en pleine mutation.</div>
  <div class="foot-url">www.novaformation.fr/maelle-dore</div>
</section>

<section class="slide c3 r2">
  <div class="title center" style="top:25px;font-size:10px">Qui Accompagnons-nous ?</div>
  <div class="ico" style="left:46px;top:58px;width:20px;height:20px;background:var(--green-dark)"><b></b></div>
  <div class="txt" style="left:30px;top:84px;width:55px">Organismes privés de formation et d'insertion professionnelle<br>Associations et dispositifs d'accompagnement de créateurs - repreneurs d'entreprises</div>
  <div class="ico" style="left:118px;top:58px;width:20px;height:20px;background:var(--green)"><b></b></div>
  <div class="txt" style="left:102px;top:84px;width:55px">Organismes publics de formation professionnelle</div>
  <div class="ico" style="left:191px;top:58px;width:20px;height:20px;background:var(--green-bright)"><b></b></div>
  <div class="txt" style="left:175px;top:84px;width:60px">Entreprises du secteur privé Salariés en mutation-transition-reconversion professionnelle</div>
  <div class="foot-logo">NOVA<i></i></div>
  <div class="foot-url">www.novaformation.fr/maelle-dore</div>
</section>

<!-- Row 3 -->
<section class="slide c1 r3">
  <div class="photo" style="left:9px;top:9px;width:90px;height:127px;background:linear-gradient(170deg,#c9d3d8,#8b7b6c 55%,#5d5248)" role="img" aria-label="Femme souriante travaillant sur son ordinateur portable dans un bureau lumineux"></div>
  <div class="title" style="left:136px;top:14px;font-size:12px">Nos leviers</div>
  <div class="bullet" style="left:140px;top:42px;width:105px">Révéler les potentiels individuels pour gagner en efficacité, aisance et confiance</div>
  <div class="bullet" style="left:140px;top:59px;width:105px">Professionnaliser les créateurs et repreneurs d'entreprises en renforçant leur leadership et posture d'employeurs</div>
  <div class="bullet" style="left:140px;top:81px;width:105px">Accompagner les acteurs de la formation /insertion professionnelle à développer l'employabilité de leurs publics</div>
  <div class="bullet" style="left:140px;top:103px;width:105px">Stimuler la créativité des managers et des équipes pour relever les défis posés par les transformations organisationnelles</div>
  <div class="foot-logo">NOVA<i></i></div>
  <div class="foot-url">www.novaformation.fr/maelle-dore</div>
</section>

<section class="slide c2 r3">
  <div class="photo" style="left:0;top:0;width:117px;bottom:0;background:linear-gradient(135deg,#2d7a35,#1c4a22 55%,#3b2c22)" role="img" aria-label="Deux personnes échangeant avec le sourire autour d'une tablette, teintées de vert"></div>
  <div class="title" style="left:15px;top:22px;font-size:9px;line-height:1.35;color:#fff">Principes de<br>management,<br>outils<br>d'accompagnement<br>et partage<br>d'expériences<br>fondent notre<br>pédagogie</div>
  <div class="bullet" style="left:129px;top:14px;width:120px">Principes de Gestion Axée sur les Résultats (GAR) appliqués à la conception, construction et mise en œuvre d'un projet professionnel.</div>
  <div class="bullet" style="left:129px;top:35px;width:120px">Méthode d'Activation du Développement Vocationnel et Personnel (ADVP) : démarche éducative qui place le sujet au centre de son expérience, de son orientation, de son développement.</div>
  <div class="bullet" style="left:129px;top:63px;width:120px">Concept de communication non violente : mode d'expression et d'écoute fondé sur l'empathie que nous utilisons pour mieux écouter et comprendre l'autre, en particulier en entreprise.</div>
  <div class="bullet" style="left:129px;top:91px;width:120px">Approche Systémique permet de développer une vision élargie des problèmes rencontrés en situation professionnelle ou personnelle.</div>
  <div class="bullet" style="left:129px;top:116px;width:120px">La maïeutique est destinée à faire exprimer un savoir caché en soi via du story telling.</div>
  <div class="foot-url">www.novaformation.fr/maelle-dore</div>
</section>

<section class="slide c3 r3">
  <div class="photo" style="left:40px;top:38px;width:180px;height:90px;background:linear-gradient(90deg,#f3f4f3,#e6e8e6,#f3f4f3)" role="img" aria-label="Carte du monde en filigrane gris"></div>
  <div class="title center" style="top:14px;font-size:10px">Nos domaines de formation</div>
  <div class="hex" style="left:16px;top:58px;background:var(--teal)"></div><div class="hex-in" style="left:16px;top:60px;color:var(--teal)">Employment</div>
  <div class="hex" style="left:72px;top:58px;background:#2a8f86"></div><div class="hex-in" style="left:72px;top:60px">SMEs</div>
  <div class="hex" style="left:128px;top:58px;background:var(--blue)"></div><div class="hex-in" style="left:128px;top:60px;color:var(--blue)">Human resources and organizational change</div>
  <div class="hex" style="left:184px;top:58px;background:var(--red)"></div><div class="hex-in" style="left:184px;top:60px;color:var(--red)">Women leadership</div>
  <div class="foot-logo">NOVA<i></i></div>
  <div class="foot-url">www.novaformation.fr/maelle-dore</div>
</section>

<!-- Row 4: catalogue -->
<section class="slide c1 r4">
  <div class="title center" style="top:13px;font-size:10px">Notre catalogue de formation</div>
  <div class="ico" style="left:30px;top:38px;background:var(--green-dark)"><b></b></div>
  <div class="cat-head" style="left:56px;top:37px;color:var(--green-dark)">Référence de missions réalisées</div>
  <div class="cat-list" style="left:58px;top:43px">1. Aenean massa.<br>2. Cum sociis natoque penatibus et dis<br>3. Parturient montes, nascetur</div>
  <div class="ico" style="left:143px;top:38px;background:var(--blue)"><b></b></div>
  <div class="cat-head" style="left:169px;top:37px;color:var(--blue)">Pays d'intervention</div>
  <div class="cat-list" style="left:171px;top:43px">1. Aenean massa.<br>2. Cum sociis natoque penatibus et dis<br>3. Parturient montes, nascetur</div>
  <div class="ico" style="left:30px;top:70px;background:var(--teal)"><b></b></div>
  <div class="cat-head" style="left:56px;top:69px;color:var(--teal)">Méthodologie</div>
  <div class="cat-list" style="left:58px;top:75px">1. Aenean massa.<br>2. Cum sociis natoque penatibus et dis<br>3. Parturient montes, nascetur</div>
  <div class="ico" style="left:143px;top:70px;background:var(--red)"><b></b></div>
  <div class="cat-head" style="left:169px;top:69px;color:var(--red)">Modalités de quitter mobilité</div>
  <div class="cat-list" style="left:171px;top:75px">1. Aenean massa.<br>2. Cum sociis natoque penatibus et dis<br>3. Parturient montes, nascetur</div>
  <div class="ico" style="left:30px;top:103px;background:var(--lime)"><b></b></div>
  <div class="cat-head" style="left:56px;top:102px;color:var(--lime)">Module durée bilingue public concerné</div>
  <div class="cat-list" style="left:58px;top:108px">1. Aenean massa.<br>2. Cum sociis natoque penatibus et dis<br>3. Parturient montes, nascetur</div>
  <div class="ico" style="left:143px;top:103px;background:var(--purple)"><b></b></div>
  <div class="cat-head" style="left:169px;top:102px;color:var(--purple)">Outils utilisés</div>
  <div class="cat-list" style="left:171px;top:108px">1. Aenean massa.<br>2. Cum sociis natoque penatibus et dis<br>3. Parturient montes, nascetur</div>
  <div class="foot-logo">NOVA<i></i></div>
  <div class="foot-url">www.novaformation.fr/maelle-dore</div>
</section>

<section class="slide c2 r4">
  <div class="title center" style="top:13px;font-size:10px">Notre catalogue de formation</div>
  <div class="ico" style="left:30px;top:38px;background:var(--green-dark)"><b></b></div>
  <div class="cat-head" style="left:56px;top:37px;color:var(--green-dark)">Référence de missions réalisées</div>
  <div class="cat-list" style="left:58px;top:43px">1. Aenean massa.<br>2. Cum sociis natoque penatibus et dis<br>3. Parturient montes, nascetur</div>
  <div class="ico" style="left:143px;top:38px;background:var(--green)"><b></b></div>
  <div class="cat-head" style="left:169px;top:37px;color:var(--green)">Pays d'intervention</div>
  <div class="cat-list" style="left:171px;top:43px">1. Aenean massa.<br>2. Cum sociis natoque penatibus et dis<br>3. Parturient montes, nascetur</div>
  <div class="ico" style="left:30px;top:70px;background:var(--green-dark)"><b></b></div>
  <div class="cat-head" style="left:56px;top:69px;color:var(--green-dark)">Méthodologie</div>
  <div class="cat-list" style="left:58px;top:75px">1. Aenean massa.<br>2. Cum sociis natoque penatibus et dis<br>3. Parturient montes, nascetur</div>
  <div class="ico" style="left:143px;top:70px;background:var(--green)"><b></b></div>
  <div class="cat-head" style="left:169px;top:69px;color:var(--green)">Modalités de quitter mobilité</div>
  <div class="cat-list" style="left:171px;top:75px">1. Aenean massa.<br>2. Cum sociis natoque penatibus et dis<br>3. Parturient montes, nascetur</div>
  <div class="ico" style="left:30px;top:103px;background:var(--green)"><b></b></div>
  <div class="cat-head" style="left:56px;top:102px;color:var(--green)">Module durée bilingue public concerné</div>
  <div class="cat-list" style="left:58px;top:108px">1. Aenean massa.<br>2. Cum sociis natoque penatibus et dis<br>3. Parturient montes, nascetur</div>
  <div class="ico" style="left:143px;top:103px;background:var(--green-bright)"><b></b></div>
  <div class="cat-head" style="left:169px;top:102px;color:var(--green-bright)">Outils utilisés</div>
  <div class="cat-list" style="left:171px;top:108px">1. Aenean massa.<br>2. Cum sociis natoque penatibus et dis<br>3. Parturient montes, nascetur</div>
  <div class="foot-logo">NOVA<i></i></div>
  <div class="foot-url">www.novaformation.fr/maelle-dore</div>
</section>

<section class="slide c3 r4">
  <div class="title center" style="top:13px;font-size:10px">Notre catalogue de formation</div>
  <div class="cat-bar" style="left:22px;top:36px;background:var(--green-dark)">Référence de missions réalisées</div>
  <div class="cat-list" style="left:42px;top:49px">1. Aenean massa.<br>2. Cum sociis natoque penatibus et dis<br>3. Parturient montes, nascetur</div>
  <div class="cat-bar" style="left:136px;top:36px;background:var(--green)">Pays d'intervention</div>
  <div class="cat-list" style="left:156px;top:49px">1. Aenean massa.<br>2. Cum sociis natoque penatibus et dis<br>3. Parturient montes, nascetur</div>
  <div class="cat-bar" style="left:22px;top:68px;background:var(--green)">Méthodologie</div>
  <div class="cat-list" style="left:42px;top:81px">1. Aenean massa.<br>2. Cum sociis natoque penatibus et dis<br>3. Parturient montes, nascetur</div>
  <div class="cat-bar" style="left:136px;top:68px;background:var(--green)">Modalités de quitter mobilité</div>
  <div class="cat-list" style="left:156px;top:81px">1. Aenean massa.<br>2. Cum sociis natoque penatibus et dis<br>3. Parturient montes, nascetur</div>
  <div class="cat-bar" style="left:22px;top:100px;background:var(--green-bright)">Module durée bilingue public concerné</div>
  <div class="cat-list" style="left:42px;top:113px">1. Aenean massa.<br>2. Cum sociis natoque penatibus et dis<br>3. Parturient montes, nascetur</div>
  <div class="cat-bar" style="left:136px;top:100px;background:var(--green-bright)">Outils utilisés</div>
  <div class="cat-list" style="left:156px;top:113px">1. Aenean massa.<br>2. Cum sociis natoque penatibus et dis<br>3. Parturient montes, nascetur</div>
  <div class="foot-logo">NOVA<i></i></div>
  <div class="foot-url">www.novaformation.fr/maelle-dore</div>
</section>

<!-- Row 5 -->
<section class="slide c1 r5">
  <div class="title center" style="top:13px;font-size:10px">Parmi nos clients...</div>
  <div class="client" style="left:18px;top:50px"><i></i>Aurea</div>
  <div class="client" style="left:66px;top:50px">Pathway Lab</div>
  <div class="client" style="left:160px;top:50px"><i></i>Kora</div>
  <div class="client" style="left:204px;top:50px">Lumen Dév</div>
  <div class="client" style="left:24px;top:86px">Solvane</div>
  <div class="client" style="left:90px;top:86px"><i></i>Tremplin</div>
  <div class="client" style="left:146px;top:86px;color:#999">Orée</div>
  <div class="client" style="left:176px;top:86px">Halden University</div>
  <div class="foot-logo">NOVA<i></i></div>
  <div class="foot-url">www.novaformation.fr/maelle-dore</div>
</section>

<section class="slide c2 r5">
  <div class="title center" style="top:10px;font-size:10px">Nos modes de formation :</div>
  <div class="title center" style="top:23px;font-size:6.5px">De loin ou de près, nous sommes à vos côtés</div>
  <div class="txt" style="left:28px;top:48px;width:55px;font-size:4.2px;text-align:justify">Nos interventions sur-mesure peuvent répondre à vos exigences logistiques. Bien que basés à Paris, nous sommes en mesure de nous déplacer en Europe et en Afrique pour assurer plusieurs formations successives.</div>
  <div class="bullet" style="left:98px;top:46px;width:50px">Echange, partage d'expériences, proximité avec les apprenants sont au cœur de nos <b>formations en présentiel.</b></div>
  <div class="bullet" style="left:98px;top:87px;width:50px">Construire du lien social et renforcer les compétences numériques à visée professionnelle sont le socle de nos formations à distance.</div>
  <div class="photo" style="left:172px;top:46px;width:66px;height:76px;background:linear-gradient(160deg,#d2d4d2,#a6aaa6)" role="img" aria-label="Carte de l'Europe et de l'Afrique en gris, France en vert"></div>
  <div style="position:absolute;left:188px;top:62px;width:7px;height:7px;background:var(--green-dark)"></div>
  <div class="foot-logo">NOVA<i></i></div>
  <div class="foot-url">www.novaformation.fr/maelle-dore</div>
</section>

<section class="slide c3 r5">
  <div class="title center" style="top:10px;font-size:10px">Nos modes de formation :</div>
  <div class="title center" style="top:23px;font-size:6.5px">De loin ou de près, nous sommes à vos côtés</div>
  <div class="txt" style="left:28px;top:48px;width:55px;font-size:4.2px;text-align:justify">Nos interventions sur-mesure peuvent répondre à vos exigences logistiques. Bien que basés à Paris, nous sommes en mesure de nous déplacer en Europe et en Afrique pour assurer plusieurs formations successives.</div>
  <div class="bullet" style="left:98px;top:46px;width:55px">Echange, partage d'expériences, proximité avec les apprenants sont au cœur de nos formations en présentiel.</div>
  <div class="bullet" style="left:98px;top:87px;width:55px">Construire du lien social et renforcer les compétences numériques à visée professionnelle sont le socle de nos formations à distance.</div>
  <div class="photo" style="left:190px;top:36px;width:50px;height:92px;background:linear-gradient(170deg,#d9dbd9,#b3b6b3)" role="img" aria-label="Carte de l'Europe et de l'Afrique en gris, France en vert"></div>
  <div style="position:absolute;left:203px;top:68px;width:6px;height:6px;background:var(--green-dark)"></div>
  <div class="foot-logo">NOVA<i></i></div>
  <div class="foot-url">www.novaformation.fr/maelle-dore</div>
</section>

<!-- Row 6: contact -->
<section class="slide c1 r6">
  <div class="title center" style="top:13px;font-size:10px">Et si on poursuivait nos échanges ?</div>
  <div class="vname" style="left:30px;top:84px">MAËLLE DORÉ</div>
  <div class="logo" style="left:38px;top:38px;font-size:26px">NOVA<i style="width:7px;height:7px"></i></div>
  <div class="tagline" style="left:38px;top:74px">FORMATION | RECONVERSION<br>UNE AUTRE VERSION DE VOUS</div>
  <div class="band" style="top:98px;height:14px">
    <span><i></i>81234567800021</span><span><i></i>+33 6 12 48 90 27</span><span><i></i>novaformation.fr/maelle-dore</span><span><i></i>contact@novaformation.fr</span>
  </div>
  <div class="foot-logo">NOVA<i></i></div>
  <div class="foot-url">www.novaformation.fr/maelle-dore</div>
</section>

<section class="slide c2 r6">
  <div class="title center" style="top:13px;font-size:10px">Et si on poursuivait nos échanges ?</div>
  <div class="vname" style="left:108px;top:84px">MAËLLE DORÉ</div>
  <div class="logo" style="left:116px;top:38px;font-size:26px">NOVA<i style="width:7px;height:7px"></i></div>
  <div class="tagline" style="left:116px;top:74px">FORMATION | RECONVERSION<br>UNE AUTRE VERSION DE VOUS</div>
  <div class="band" style="top:98px;height:14px">
    <span><i></i>81234567800021</span><span><i></i>+33 6 12 48 90 27</span><span><i></i>novaformation.fr/maelle-dore</span><span><i></i>contact@novaformation.fr</span>
  </div>
  <div class="foot-logo">NOVA<i></i></div>
  <div class="foot-url">www.novaformation.fr/maelle-dore</div>
</section>

<section class="slide c3 r6">
  <div class="contact-col" style="position:absolute;left:0;top:0;width:123px;bottom:0;background:var(--green-dark);color:#fff;font-size:4px;display:flex;flex-direction:column;justify-content:space-around;padding:14px 14px 20px">
    <span><i style="width:7px;height:7px"></i>81234567800021</span>
    <span><i style="width:7px;height:7px"></i>+33 6 12 48 90 27</span>
    <span><i style="width:7px;height:7px"></i>novaformation.fr/maelle-dore</span>
    <span><i style="width:7px;height:7px"></i>contact@novaformation.fr</span>
  </div>
  <div class="title" style="left:145px;top:20px;font-size:10px;line-height:1.2">Et si on poursuivait<br>nos échanges ?</div>
  <div class="vname" style="left:145px;top:106px">MAËLLE DORÉ</div>
  <div class="logo" style="left:152px;top:58px;font-size:24px">NOVA<i style="width:7px;height:7px"></i></div>
  <div class="tagline" style="left:152px;top:92px">FORMATION | RECONVERSION<br>UNE AUTRE VERSION DE VOUS</div>
  <div class="foot-url">www.novaformation.fr/maelle-dore</div>
</section>

<!-- Row 7 -->
<section class="slide c1 r7">
  <div class="title center" style="top:13px;font-size:10px">Nous les avons accompagnés, Elles/Ils témoignent”</div>
  <div class="foot-logo">NOVA<i></i></div>
  <div class="foot-url">www.novaformation.fr/maelle-dore</div>
</section>

<section class="slide c2 r7">
  <div class="title" style="left:22px;top:88px;font-size:12px;line-height:1.45">La roue<br>vertueuse</div>
  <svg style="position:absolute;left:120px;top:14px" width="116" height="116" viewBox="0 0 116 116">
    <g transform="rotate(-90 58 58)" fill="none" stroke-width="22">
      <circle cx="58" cy="58" r="46" stroke="var(--green-dark)" stroke-dasharray="35 254" stroke-dashoffset="0"/>
      <circle cx="58" cy="58" r="46" stroke="var(--green)" stroke-dasharray="35 254" stroke-dashoffset="-36"/>
      <circle cx="58" cy="58" r="46" stroke="var(--green)" stroke-dasharray="35 254" stroke-dashoffset="-72"/>
      <circle cx="58" cy="58" r="46" stroke="var(--green-bright)" stroke-dasharray="35 254" stroke-dashoffset="-108"/>
      <circle cx="58" cy="58" r="46" stroke="#3fd64f" stroke-dasharray="35 254" stroke-dashoffset="-144"/>
      <circle cx="58" cy="58" r="46" stroke="#a8a8a8" stroke-dasharray="35 254" stroke-dashoffset="-180"/>
      <circle cx="58" cy="58" r="46" stroke="#c4c4c4" stroke-dasharray="35 254" stroke-dashoffset="-216"/>
      <circle cx="58" cy="58" r="46" stroke="#d9d9d9" stroke-dasharray="35 254" stroke-dashoffset="-252"/>
    </g>
    <g font-size="2.8" font-family="Kaushan Script, cursive" text-anchor="middle">
      <text x="70" y="18" fill="#fff">Développer</text>
      <text x="98" y="42" fill="#fff">Identifier</text>
      <text x="99" y="76" fill="#fff">Renforcer</text>
      <text x="75" y="102" fill="#fff">Élaborer</text>
      <text x="42" y="102" fill="#333">Valoriser</text>
      <text x="17" y="76" fill="#333">S'approprier</text>
      <text x="18" y="42" fill="#333">Stimuler</text>
      <text x="44" y="18" fill="#fff">Identifier</text>
    </g>
  </svg>
  <div class="foot-logo">NOVA<i></i></div>
  <div class="foot-url">www.novaformation.fr/maelle-dore</div>
</section>

<section class="slide c3 r7">
  <div style="position:absolute;left:10px;top:0;width:68px;height:132px;background:var(--green-dark);color:#fff;padding:60px 5px 0">
    <div style="font-family:'Kaushan Script',cursive;font-size:13px;margin-bottom:4px">Nos outils</div>
    <div style="font-size:4px;line-height:1.3">Nous disposons d'une large palette d'outils méthodologiques et courants d'intervention sur lesquels nous appuyons nos interventions.</div>
  </div>
  <div class="bullet" style="left:90px;top:18px;width:155px;text-align:justify"><b>L'approche Systémique</b>, issue des recherches de l'école de Vallombre dans les années 50/70 permet de développer une vision élargie des problèmes rencontrés en situation professionnelle ou personnelle et d'envisager des solutions nouvelles à ces difficultés.</div>
  <div class="bullet" style="left:90px;top:48px;width:155px;text-align:justify"><b>La communication non violente (CNV)</b> développée par Martin B. Roussel est un mode d'expression et d'écoute fondé sur l'empathie. Nous l'utilisons comme une technique à la fois pertinente et très simple, mieux écouter et comprendre l'autre, en particulier en entreprise.</div>
  <div class="bullet" style="left:90px;top:80px;width:155px;text-align:justify"><b>La Méthode ADVP</b> : L'Activation du Développement Vocationnel et Personnel part du principe que toute personne est capable d'agir sur son devenir. C'est une démarche éducative qui place le sujet au centre de son expérience, de son orientation, de son développement.</div>
  <div class="bullet" style="left:90px;top:112px;width:155px;text-align:justify"><b>La Maïeutique</b> : La maïeutique consiste à faire accoucher les esprits de leurs connaissances. Elle est destinée à faire exprimer un savoir caché en soi.</div>
  <div class="foot-logo">NOVA<i></i></div>
  <div class="foot-url">www.novaformation.fr/maelle-dore</div>
</section>

</body>
</html>
```